Lumora Flow Collective Business Cards

I need business cards for staff in a new startup. Our company name is MorvaLeap - we train Tai Chi teachers. But our biggest project is called Lumora Flow Collective - a federal project to put together free Tai Chi classes for Vets all across America. It's a young company, with a spirit of excitement, passion, a desire to do good for others (our Vets) and a modern style and sensibility. In other words, not old-fashioned Asian martial arts theme, but something new.

Industry/Entity Type

Health And Wellness

Contact Information for Business Card

The topic is ancient healing, but the company is the Quibbletons - so I'd like a card design that captures that.

Font styles to use
Sans Serif

Colors

Designer to choose colors to be used in the design.

Requirements
Nice to have
• I've got two logos - one for the company and one for the project. I want to see if we can incorporate them both without it becoming too busy.
Should not have
• Overly old-fashioned yin-yang themes.

```html
<!DOCTYPE html>
<html lang="en">
<head>
<meta charset="utf-8">
<title>Lumora Flow Collective – Business Cards</title>
<link href="https://fonts.googleapis.com/css2?family=Lato:wght@400;700;900&display=swap" rel="stylesheet">
<style>
  :root{
    --bg:#e9e9ec;
    --card:#ffffff;
    --navy:#262a78;
    --red:#e5252f;
    --rule:#2340a6;
    --ink:#1c1c1c;
    --shadow:rgba(0,0,0,.14);
  }
  *{box-sizing:border-box;margin:0;padding:0}
  html,body{width:1200px;height:1200px;overflow:hidden;background:var(--bg)}
  body{font-family:"Lato",sans-serif;color:var(--ink);position:relative}
  .card{
    position:absolute;left:150px;width:900px;height:514px;
    background:var(--card);border-radius:34px;
    box-shadow:0 10px 30px var(--shadow);overflow:hidden;
  }
  .card--front{top:56px}
  .card--back{top:630px}

  .brand{position:absolute;display:flex;align-items:center;gap:14px}
  .brand__dot{width:18px;height:18px;border-radius:50%;flex:none}
  .brand__name{font-weight:400;letter-spacing:.04em;white-space:nowrap}
  .brand--project .brand__dot{background:var(--navy)}
  .brand--project .brand__name{color:var(--navy)}
  .brand--company .brand__dot{background:var(--red)}
  .brand--company .brand__name{color:var(--red)}

  .card--front .brand--project{left:120px;top:318px}
  .card--front .brand--project .brand__name{font-size:34px}
  .card--front .brand--company{right:90px;top:140px}
  .card--front .brand--company .brand__name{font-size:40px}

  .card--back .brand--project{left:70px;top:118px}
  .card--back .brand--project .brand__name{font-size:32px}
  .card--back .brand--company{right:80px;top:56px}
  .card--back .brand--company .brand__name{font-size:36px}

  .divider{position:absolute;left:70px;right:60px;top:250px;height:2px;background:var(--rule)}

  .person{position:absolute;left:70px;top:286px}
  .person__name{font-size:30px;font-weight:900;color:var(--red);letter-spacing:.01em;text-transform:uppercase}
  .person__role{font-size:17px;color:var(--ink);margin-top:2px}

  .contacts{position:absolute;left:70px;top:370px;list-style:none}
  .contacts li{display:flex;align-items:center;gap:12px;font-size:19px;line-height:28px}
  .contacts svg{width:16px;height:16px;flex:none;fill:var(--navy)}

  .address{position:absolute;right:60px;top:290px;text-align:right;font-size:20px;line-height:28px}
</style>
</head>
<body>

<section class="card card--front" aria-label="Card front">
  <div class="brand brand--project">
    <span class="brand__dot"></span>
    <span class="brand__name">Lumora Flow Collective</span>
  </div>
  <div class="brand brand--company">
    <span class="brand__dot"></span>
    <span class="brand__name">MorvaLeap</span>
  </div>
</section>

<section class="card card--back" aria-label="Card back">
  <div class="brand brand--project">
    <span class="brand__dot"></span>
    <span class="brand__name">Lumora Flow Collective</span>
  </div>
  <div class="brand brand--company">
    <span class="brand__dot"></span>
    <span class="brand__name">MorvaLeap</span>
  </div>

  <div class="divider"></div>

  <div class="person">
    <p class="person__name">Dorian Maflet</p>
    <p class="person__role">Manager</p>
  </div>

  <ul class="contacts">
    <li><svg viewBox="0 0 16 16"><path d="M4 1h8a1 1 0 0 1 1 1v12a1 1 0 0 1-1 1H4a1 1 0 0 1-1-1V2a1 1 0 0 1 1-1zm1 2v9h6V3z"/></svg>000 - 000 - 0000</li>
    <li><svg viewBox="0 0 16 16"><path d="M3.5 1.5l2.5 0 1.2 3.2-1.7 1.2a8 8 0 0 0 4.6 4.6l1.2-1.7 3.2 1.2v2.5a1.5 1.5 0 0 1-1.6 1.5A12.5 12.5 0 0 1 2 3.1 1.5 1.5 0 0 1 3.5 1.5z"/></svg>000 - 000 - 0000</li>
    <li><svg viewBox="0 0 16 16"><path d="M1 3h14v10H1zm1.5 1.5v.3L8 8.6l5.5-3.8v-.3zM2.5 6.6v5h11v-5L8 10.4z"/></svg>info@mailaddress.com</li>
    <li><svg viewBox="0 0 16 16"><path d="M8 1a7 7 0 1 0 0 14A7 7 0 0 0 8 1zm0 1.5c.9 0 1.8 1.7 2 4.5H6c.2-2.8 1.1-4.5 2-4.5zM2.6 7h2c.1-1.6.4-3 .9-4A5.5 5.5 0 0 0 2.6 7zm8.8 0h2a5.5 5.5 0 0 0-2.9-4c.5 1 .8 2.4.9 4zM2.6 9a5.5 5.5 0 0 0 2.9 4c-.5-1-.8-2.4-.9-4zM6 9c.2 2.8 1.1 4.5 2 4.5s1.8-1.7 2-4.5zm5.4 0c-.1 1.6-.4 3-.9 4a5.5 5.5 0 0 0 2.9-4z"/></svg>www.websitehere.com</li>
  </ul>

  <address class="address" style="font-style:normal">
    47 Calder Ridge Lane<br>
    Suite 210 Brenwick, CT 06192
  </address>
</section>

</body>
</html>
```